Training company needs a Quick Reference Card design

We have draft skeleton of the design and most of the text. But we need a designer to take it the rest if the way.
I have designed a 2 page quick reference card - it is meant to be a 2-sided document. The first page is portrait, the back page can either be portrait or landscape, I'm not too concerned, whichever fits best.
Section called 'Maps' on front, a map is a collection of documents (like a manual), a topic is a document (like a page or section of a manual) and a block is a section of a document. The graphic is mean to illustrate the hierarchy but essentially a map is a big document with smaller documents in it.
Please use the company's logo colors to differentiate the different sections with minimal/ highlight only use of the darkest color, preferably.
Please use the icons for the corresponding Information types in the chart of the back - except please re-design the icons color scheme to match the company's logo/website colors.

Target Market(s)

Technical writers, after attending our training course, as an ongoing resource for them

Industry/Entity Type

It Company

Font styles to use
Sans Serif

Requirements
Must have
• Must adhere to look and feel of brand/ website. www.lumarockwise.com
Nice to have
• Please keep the design modern and slick looking, not too busy, easy to read

```html
<!DOCTYPE html>
<html lang="en">
<head>
<meta charset="utf-8">
<title>Quick Reference Card – Lumarockwise</title>
<link rel="stylesheet" href="https://fonts.googleapis.com/css2?family=Quicksand:wght@500;700&family=Nunito:wght@600;700;800&display=swap">
<style>
  :root {
    --navy: #241b8e;
    --navy-deep: #1d1577;
    --cyan: #0aa6da;
    --cyan-light: #12b3e4;
    --white: #ffffff;
    --paper: #ffffff;
    --head-font: "Quicksand", sans-serif;
    --body-font: "Nunito", sans-serif;
  }
  * { box-sizing: border-box; margin: 0; padding: 0; }
  html, body { width: 887px; height: 1200px; overflow: hidden; background: var(--paper); }
  .card { position: relative; width: 887px; height: 1200px; font-family: var(--body-font); color: var(--white); }
  .panel { position: absolute; border-radius: 5px; }
  .navy { background: var(--navy); }
  .cyan { background: var(--cyan); }
  .center { text-align: center; }

  /* header */
  .brand { position: absolute; left: 16px; top: 16px; width: 250px; display: flex; align-items: center; gap: 12px; }
  .brand-dot { flex: none; width: 64px; height: 64px; border-radius: 50%; background: var(--cyan); }
  .brand-name { font-family: var(--head-font); font-weight: 700; font-size: 23px; color: var(--navy); line-height: 1.05; letter-spacing: 0.5px; }
  .header-divider { position: absolute; left: 276px; top: 20px; width: 3px; height: 64px; background: var(--navy); }
  .title { position: absolute; left: 294px; top: 26px; font-family: var(--head-font); font-weight: 700; font-size: 43px; line-height: 52px; letter-spacing: 2.5px; color: var(--navy); white-space: nowrap; }
  .title .accent { color: var(--cyan); }
  .rule { position: absolute; left: 9px; width: 869px; height: 2px; background: var(--cyan); }

  /* map */
  .map { left: 9px; top: 124px; width: 409px; height: 287px; }
  .map-title { position: absolute; left: 0; right: 0; top: 10px; font-family: var(--head-font); font-weight: 700; font-size: 26px; }
  .topic-label { position: absolute; top: 66px; width: 161px; font-family: var(--head-font); font-weight: 700; font-size: 23px; text-align: center; }
  .block { position: absolute; width: 161px; height: 79px; background: var(--cyan); display: flex; align-items: center; justify-content: center; text-align: center; font-family: var(--head-font); font-weight: 700; font-size: 18px; line-height: 1.25; }
  .definitions { left: 426px; top: 124px; width: 452px; height: 287px; padding: 22px 24px; font-size: 15.5px; line-height: 1.45; font-weight: 600; text-align: center; }
  .definitions p + p { margin-top: 16px; }
  .definitions strong { font-weight: 800; }

  /* section bars */
  .bar { position: absolute; left: 6px; width: 872px; border-radius: 5px; background: var(--navy); font-family: var(--head-font); font-weight: 700; font-size: 26px; text-align: center; letter-spacing: 0.5px; }
  .area { position: absolute; left: 6px; width: 872px; background: var(--cyan); border-radius: 0 0 5px 5px; }
  .col { position: absolute; top: 16px; text-align: center; }
  .col h3 { font-family: var(--head-font); font-weight: 700; font-size: 23px; line-height: 1.2; margin-bottom: 10px; }
  .col p { font-size: 15.5px; line-height: 1.45; font-weight: 700; }

  /* questions */
  .questions { left: 9px; top: 698px; width: 493px; height: 218px; padding: 22px 20px; }
  .questions h3 { font-family: var(--head-font); font-weight: 700; font-size: 22px; line-height: 1.2; text-align: center; margin-bottom: 14px; }
  .questions ol { list-style: none; font-size: 18px; font-weight: 600; line-height: 1.4; }
  .questions li { display: flex; gap: 14px; margin-bottom: 8px; }
  .questions .num { width: 22px; flex: none; }
  .arts { left: 508px; top: 698px; width: 370px; height: 218px; padding: 20px 14px; text-align: center; }
  .arts h3 { font-family: var(--head-font); font-weight: 700; font-size: 22px; line-height: 1.2; }
  .arts .acronym { font-family: var(--head-font); font-weight: 700; font-size: 25px; margin-top: 4px; }
  .arts p { font-size: 17px; font-weight: 600; line-height: 1.25; }
</style>
</head>
<body>
<main class="card">
  <header>
    <div class="brand"><span class="brand-dot"></span><span class="brand-name">LUMAROCK<br>WISE.com</span></div>
    <div class="header-divider"></div>
    <h1 class="title">QUICK REFERENCE <span class="accent">CARD</span></h1>
  </header>
  <div class="rule" style="top:103px"></div>
  <div class="rule" style="top:110px"></div>

  <section class="panel navy map">
    <h2 class="map-title center">MAP</h2>
    <div class="topic-label" style="left:18px">TOPIC</div>
    <div class="topic-label" style="left:216px">TOPIC</div>
    <div class="block" style="left:18px; top:98px">PRIMARY<br>BLOCK</div>
    <div class="block" style="left:216px; top:98px">PRIMARY<br>BLOCK</div>
    <div class="block" style="left:18px; top:188px">SUB-BLOCK</div>
    <div class="block" style="left:216px; top:188px">SUB-BLOCK</div>
  </section>

  <section class="panel cyan definitions">
    <p><strong>A map</strong> is a file that organizes topics into structured collections of information. Maps specify hierarchy and relationships among topics.</p>
    <p><strong>A topic</strong> is a group of related blocks with a title. Use the chunking principle to group together relevant blocks.</p>
    <p><strong>A block</strong> is a bite-sized chunk of information about one main idea that allows the writer to organize the material into logical sections.</p>
  </section>

  <h2 class="bar" style="top:423px; height:47px; line-height:47px">GENERAL WRITING RULES</h2>
  <section class="area" style="top:470px; height:217px">
    <div class="col" style="left:20px; width:260px">
      <h3>EFFECTIVE<br>SENTENCES</h3>
      <p>One main agent, action &amp; outcome. Use active voice and simplest tense possible. No more than 7 sentences per paragraph. Use lists and tables.</p>
    </div>
    <div class="col" style="left:306px; width:260px">
      <h3>SPECIAL<br>CHARACTERS</h3>
      <p>Avoid special characters, spell out words instead. Remove parentheses, colons and dashes. Avoid using quotation marks and slashes.</p>
    </div>
    <div class="col" style="left:600px; width:250px">
      <h3>PLAIN<br>LANGUAGE</h3>
      <p>Write in short sentences. Provide useful titles. Use clear familiar words. Avoid excess words.<br>Be consistent.</p>
    </div>
  </section>

  <section class="panel navy questions">
    <h3>3 QUESTIONS TO ASK BEFORE<br>YOU START WRITING</h3>
    <ol>
      <li><span class="num">1.</span><span>What is the purpose of this information?</span></li>
      <li><span class="num">2.</span><span>What is the desired user response of this information?</span></li>
      <li><span class="num">3.</span><span>Who is the audience?</span></li>
    </ol>
  </section>

  <section class="panel navy arts">
    <h3>2 TYPES OF<br>LANGUAGE ARTS:</h3>
    <div class="acronym">LAFI</div>
    <p>Language arts for information</p>
    <div class="acronym">LAFPR</div>
    <p>language arts for personal<br>response</p>
  </section>

  <h2 class="bar" style="top:925px; height:46px; line-height:46px">4 COGNITIVE PRINCIPLES</h2>
  <section class="area" style="top:971px; height:219px">
    <div class="col" style="left:10px; width:200px">
      <h3>CONSISTENCY</h3>
      <p>Use similar terms and structures. Pick a term and stick with it. Use the same sequence of blocks. Use consistent styles.</p>
    </div>
    <div class="col" style="left:228px; width:190px">
      <h3>CHUNKING</h3>
      <p>Maximum of nine (7 +/- 2) items in a list, rows in a table, blocks in a topic, or topics in a map.</p>
    </div>
    <div class="col" style="left:438px; width:200px">
      <h3>RELEVANCE</h3>
      <p>Group similar items together. Separate relevance? Separate block. Irrelevant? Delete it.</p>
    </div>
    <div class="col" style="left:655px; width:200px">
      <h3>TITLING</h3>
      <p>Name everything. Name every block, every topic, every map and every table column.</p>
    </div>
  </section>
</main>
</body>
</html>
```